NEW YORK Plumbing/utility company 10 year anniversary business card

Looking For simple back and front business card would like to include a few things in description
We offer 24/7 emergency service
residential
commercial
industrial
municipal
services offered
Plumbing
hydro excavation
hydro jetting
Well pumps
Sewer pumps
water mains
sewer mains

```html
<!DOCTYPE html>
<html lang="en">
<head>
<meta charset="utf-8">
<title>Kestrel Valley Water &amp; Sewer — Business Card</title>
<link href="https://fonts.googleapis.com/css2?family=Roboto+Condensed:wght@400;700&family=Roboto:wght@400;500&display=swap" rel="stylesheet">
<style>
  :root {
    --page-bg: #e4e6e8;
    --brand-blue: #0f5aa0;
    --navy: #1f3a8a;
    --deep-blue: #1b4fa8;
    --sky: #cfe5f7;
    --alert-red: #e2232a;
    --name-orange: #f47a20;
    --ink-grey: #3d3d3d;
    --gold: #c9a23a;
    --white: #ffffff;
  }
  * { box-sizing: border-box; margin: 0; padding: 0; }
  html, body { width: 1200px; height: 1200px; overflow: hidden; }
  body { background: var(--page-bg); position: relative; font-family: "Roboto", Arial, sans-serif; }

  .card {
    position: absolute; left: 247px; width: 720px; height: 480px; overflow: hidden;
    background: linear-gradient(160deg, var(--sky) 0%, #eef6fd 35%, var(--white) 60%, #e6f1fb 100%);
    box-shadow: 0 6px 14px rgba(0,0,0,.25);
  }
  .card--front { top: 130px; }
  .card--back { top: 646px; }

  .water {
    position: absolute; left: 0; right: 0; bottom: 0;
    background: linear-gradient(180deg, rgba(170,210,240,0) 0%, #6fb0e3 22%, #2f7fd0 55%, var(--deep-blue) 100%);
  }
  .card--front .water { top: 260px; }
  .card--back .water { top: 200px; background: linear-gradient(180deg, rgba(170,210,240,0) 0%, #7bb6e6 22%, #3d86d2 50%, var(--navy) 100%); }

  .brand { position: absolute; color: var(--brand-blue); font-family: "Roboto Condensed", Arial, sans-serif; font-weight: 700; text-transform: uppercase; line-height: 1; display: flex; align-items: center; gap: 14px; }
  .brand__mark { width: 22px; height: 22px; border-radius: 50%; background: var(--brand-blue); flex: none; }
  .brand__name { display: block; }
  .brand__sub { display: block; }
  .card--front .brand { left: 185px; top: 80px; }
  .card--front .brand__name { font-size: 58px; letter-spacing: 1px; }
  .card--front .brand__sub { font-size: 27px; letter-spacing: 4px; margin-top: 10px; text-align: center; }
  .card--back .brand { left: 74px; top: 62px; gap: 10px; }
  .card--back .brand__mark { width: 18px; height: 18px; }
  .card--back .brand__name { font-size: 43px; }
  .card--back .brand__sub { font-size: 21px; letter-spacing: 3px; margin-top: 8px; text-align: center; }

  .anniversary-badge { position: absolute; left: 552px; top: 134px; width: 126px; height: 118px; }

  .emergency {
    position: absolute; left: 0; right: 0; top: 352px; text-align: center;
    font-family: "Roboto Condensed", Arial, sans-serif; font-weight: 700; font-size: 33px;
    color: var(--alert-red); text-transform: uppercase; letter-spacing: -0.3px;
    -webkit-text-stroke: 1px var(--white); paint-order: stroke fill;
    text-shadow: 0 0 2px var(--white), 0 0 2px var(--white);
  }
  .sectors {
    position: absolute; left: 40px; right: 40px; top: 403px; display: flex; justify-content: space-between;
    font-family: "Roboto Condensed", Arial, sans-serif; font-weight: 700; font-size: 27px;
    color: var(--white); text-transform: uppercase; list-style: none;
    text-shadow: 0 0 3px #0b2f73, 1px 1px 1px #0b2f73;
  }

  .contact { position: absolute; right: 45px; top: 52px; text-align: right; }
  .contact__name { font-family: "Roboto", Arial, sans-serif; font-weight: 500; font-size: 36px; color: var(--name-orange); line-height: 1.1; }
  .contact__title { font-size: 22px; color: var(--ink-grey); margin-top: 2px; }
  .contact__phones { list-style: none; margin-top: 18px; margin-right: 10px; font-size: 23px; color: var(--ink-grey); line-height: 28px; }

  .services { position: absolute; left: 72px; top: 284px; color: var(--white); font-family: "Roboto Condensed", Arial, sans-serif; }
  .services__title { font-weight: 700; font-size: 26px; text-transform: uppercase; }
  .services__cols { display: flex; gap: 22px; margin-top: 10px; }
  .services__list { list-style: none; font-size: 22px; text-transform: uppercase; line-height: 28px; }
  .services__list--right { margin-top: 3px; }
  .services__list li { position: relative; padding-left: 20px; }
  .services__list li::before { content: ""; position: absolute; left: 0; top: 10px; width: 9px; height: 9px; border-radius: 50%; background: var(--alert-red); }
</style>
</head>
<body>

<section class="card card--front" aria-label="Business card front">
  <div class="water" role="img" aria-label="Photograph of a clear blue water surface with bubbles"></div>
  <div class="brand">
    <div>
      <span class="brand__name">Kestrel Valley</span>
      <span class="brand__sub">Water &amp; Sewer</span>
    </div>
  </div>
  <svg class="anniversary-badge" viewBox="0 0 126 118" role="img" aria-label="Gold ten-year anniversary badge">
    <circle cx="63" cy="59" r="56" fill="var(--gold)"/>
  </svg>
  <p class="emergency">We Offer 24/7 Emergency Service</p>
  <ul class="sectors">
    <li>Residential</li>
    <li>Commercial</li>
    <li>Industrial</li>
    <li>Municipal</li>
  </ul>
</section>

<section class="card card--back" aria-label="Business card back">
  <div class="water" role="img" aria-label="Photograph of a clear blue water surface with bubbles"></div>
  <div class="brand">
    <div>
      <span class="brand__name">Kestrel Valley</span>
      <span class="brand__sub">Water &amp; Sewer</span>
    </div>
  </div>
  <div class="contact">
    <p class="contact__name">Daniel Porter</p>
    <p class="contact__title">Managing Director</p>
    <ul class="contact__phones">
      <li>(555) 014-2387</li>
      <li>+1 555 019 8446</li>
    </ul>
  </div>
  <div class="services">
    <h2 class="services__title">Services Offered</h2>
    <div class="services__cols">
      <ul class="services__list">
        <li>Plumbing</li>
        <li>Hydro Excavation</li>
        <li>Hydro Jetting</li>
        <li>Well Pumps</li>
      </ul>
      <ul class="services__list services__list--right">
        <li>Sewer Pumps</li>
        <li>Water Mains</li>
        <li>Sewer Mains</li>
      </ul>
    </div>
  </div>
</section>

</body>
</html>
```